Board to put on a meditation centre - Lantern Grove

I need a board design for a new meditation centre based in Oslo which offers free courses in meditation and self-empowerment. The size of the board is width 374cm x height 104cm.  The name of the meditation centre together with subtitles should be on the board but also some elegant decoration that matches the theme (lantern grove/meditation).
Here is the website of the meditation centre to give you a feeling of it: https://lyktelundsenteret.no/
Good if you can use a blue color close to this one: rgb(37, 180, 193) as well as some brown/golden color (similar to the palette on the website).
On the board it should say:
Lyktelunden (in big letters, the rest is subtitles)
Meditasjon & Spirituell visdom
Kurs - Retreat - Dialog
lyktelundsenteret.no
The design should be very elegant and beautiful and the feeling should be of "An Lantern Grove". A logo is here attached and should be used but I need to get a better quality version of it, will upload that as soon as possible.

```html
<!DOCTYPE html>
<html lang="no">
<head>
<meta charset="UTF-8">
<title>Lyktelunden – skilt</title>
<link rel="stylesheet" href="https://fonts.googleapis.com/css2?family=Oswald:wght@500&family=Montserrat:wght@500;600;800&display=swap">
<style>
  :root {
    --teal: #25b4c1;
    --teal-deep: #12878f;
    --ink: #2b2b2b;
    --tan: #b9aa98;
    --tan-soft: #d3c8ba;
    --paper: #ffffff;
    --backdrop: #f3f3f2;
    --accent-red: #d8283f;
  }
  * { box-sizing: border-box; margin: 0; padding: 0; }
  html, body {
    width: 1110px; height: 1200px; overflow: hidden;
    background: var(--backdrop);
  }
  .stage {
    width: 1110px; height: 1200px;
    display: flex; align-items: center; justify-content: center;
  }
  .board {
    position: relative;
    width: 1000px; height: 278px;
    background: var(--paper);
    box-shadow: 0 12px 30px rgba(0,0,0,0.12);
    overflow: hidden;
  }
  .board-art { position: absolute; inset: 0; width: 1000px; height: 278px; }
  .content {
    position: absolute; left: 57px; top: 30px;
    font-family: "Montserrat", sans-serif;
    color: var(--ink);
  }
  .title {
    font-family: "Oswald", sans-serif;
    font-weight: 500;
    font-size: 96px; line-height: 1;
    letter-spacing: -0.5px;
    white-space: nowrap;
  }
  .title .part-a { color: var(--teal); }
  .title .part-b { color: var(--ink); }
  .subtitle {
    margin-top: 4px;
    font-weight: 800; font-size: 27px; letter-spacing: 0.3px;
    line-height: 1.1;
    text-transform: uppercase;
    white-space: nowrap;
  }
  .offers {
    list-style: none;
    display: flex; gap: 34px; margin-top: 8px;
    font-weight: 600; font-size: 30px; line-height: 1.2;
  }
  .offer { display: flex; align-items: center; gap: 8px; }
  .offer svg { width: 30px; height: 28px; }
  .footer {
    display: flex; align-items: center; gap: 16px;
    margin-top: 14px;
  }
  .org { display: flex; align-items: center; gap: 6px;
    font-weight: 500; font-size: 12px; letter-spacing: 1.6px;
    color: var(--ink); text-transform: uppercase; }
  .org-dot { width: 24px; height: 24px; border-radius: 50%; background: var(--accent-red); }
  .web { display: flex; align-items: center; gap: 6px;
    font-weight: 600; font-size: 17px; color: var(--ink); }
  .web svg { width: 18px; height: 18px; }
</style>
</head>
<body>
<main class="stage">
  <section class="board">
    <svg class="board-art" viewBox="0 0 1000 278">
      <defs>
        <linearGradient id="tealFill" x1="0" y1="0" x2="1" y2="1">
          <stop offset="0" stop-color="#2bbac6"/>
          <stop offset="1" stop-color="#10838c"/>
        </linearGradient>
        <radialGradient id="photoFill" cx="0.5" cy="0.45" r="0.55">
          <stop offset="0" stop-color="#a6e3e7"/>
          <stop offset="0.5" stop-color="#5ccbd3" stop-opacity="0.85"/>
          <stop offset="1" stop-color="#25b4c1" stop-opacity="0"/>
        </radialGradient>
        <pattern id="dots" width="9" height="9" patternUnits="userSpaceOnUse">
          <circle cx="4.5" cy="4.5" r="1.8" fill="none" stroke="#c2b5a5" stroke-width="0.8"/>
        </pattern>
      </defs>
      <rect x="2" y="2" width="36" height="54" fill="url(#dots)"/>
      <rect x="538" y="198" width="36" height="54" fill="url(#dots)"/>
      <path d="M662 0 C700 30 722 80 706 130 C734 80 720 30 692 0 Z" fill="var(--tan)"/>
      <path d="M688 0 H1000 V278 H598 C604 222 640 192 680 160 C722 126 732 60 688 0 Z" fill="url(#tealFill)"/>
      <path d="M592 278 C594 250 598 232 606 214" fill="none" stroke="var(--tan-soft)" stroke-width="1.5"/>
      <g role="img" aria-label="Photograph of a woman meditating in lotus pose with hands raised, set in front of a large white line-art mandala">
        <rect x="690" y="0" width="310" height="278" fill="url(#photoFill)"/>
      </g>
    </svg>

    <div class="content">
      <h1 class="title"><span class="part-a">LYKTE</span><span class="part-b">LUNDEN</span></h1>
      <p class="subtitle">Meditasjon &amp; Spirituell Visdom</p>
      <ul class="offers">
        <li class="offer">
          <svg viewBox="0 0 30 28"><rect x="4" y="4" width="22" height="15" rx="2" fill="var(--teal)"/><rect x="8" y="8" width="14" height="2" fill="#fff"/><rect x="8" y="12" width="10" height="2" fill="#fff"/><rect x="2" y="20" width="26" height="4" rx="1" fill="var(--tan)"/></svg>
          Kurs
        </li>
        <li class="offer">
          <svg viewBox="0 0 30 28"><path d="M15 3 C21 9 21 18 15 24 C9 18 9 9 15 3 Z" fill="var(--tan)"/><path d="M4 10 C11 12 14 18 14 25 C7 23 4 17 4 10 Z" fill="var(--teal)"/><path d="M26 10 C19 12 16 18 16 25 C23 23 26 17 26 10 Z" fill="var(--teal)"/></svg>
          Retreat
        </li>
        <li class="offer">
          <svg viewBox="0 0 30 28"><rect x="2" y="2" width="19" height="15" rx="2" fill="var(--tan)"/><rect x="6" y="6" width="11" height="2" fill="#fff"/><rect x="6" y="10" width="8" height="2" fill="#fff"/><path d="M12 12 H27 V23 H24 V27 L19 23 H12 Z" fill="var(--teal)"/></svg>
          Dialog
        </li>
      </ul>
      <div class="footer">
        <div class="org"><span class="org-dot"></span>Stillhavn</div>
        <div class="web">
          <svg viewBox="0 0 18 18"><circle cx="9" cy="9" r="8" fill="none" stroke="var(--teal)" stroke-width="2"/><circle cx="9" cy="9" r="4.5" fill="var(--ink)"/></svg>
          lyktelundsenteret.no
        </div>
      </div>
    </div>
  </section>
</main>
</body>
</html>
```